Business Card Design

We are a florist shop that also stocks a range of giftware and jewellery. I would like a new design that incorporates a light green background. If you could use a skeleton leaf somewhere in the design that would be great. I would also like to incorporate the find us on Friendlink logo on this design.

Industry/Entity Type

Florist

Contact Information for Business Card

Petals on Larkmore
41 Brindle street
Ashvale Marrow 3871
Phone: 0352983047
Fax : 0352983066
email: pol@wrenmail.net.au

Proprietors : Dana & Lee Thornwick

```html
<!DOCTYPE html>
<html lang="en">
<head>
<meta charset="utf-8">
<title>Petals on Larkmore – Business Card</title>
<link href="https://fonts.googleapis.com/css2?family=Marcellus&family=Jost:wght@300;400;600&display=swap" rel="stylesheet">
<style>
  :root {
    --card-white: #ffffff;
    --ink: #111111;
    --florist-green: #1f5a3e;
    --sage-panel: #dfe6e0;
    --sage-vein: #eef2ee;
    --badge-dark: #1a1a1a;
  }
  * { margin: 0; padding: 0; box-sizing: border-box; }
  html, body {
    width: 1200px;
    height: 758px;
    overflow: hidden;
    background: var(--card-white);
  }
  .card {
    position: relative;
    width: 1200px;
    height: 758px;
    background: var(--card-white);
    font-family: "Jost", sans-serif;
    color: var(--ink);
  }
  .leaf-panel {
    position: absolute;
    left: 607px;
    top: 0;
    width: 593px;
    height: 758px;
    background: linear-gradient(160deg, var(--sage-vein) 0%, var(--sage-panel) 35%, var(--sage-panel) 70%, var(--sage-vein) 100%);
  }
  .brand {
    position: absolute;
    left: 48px;
    top: 72px;
    width: 520px;
    font-family: "Marcellus", serif;
    font-weight: 400;
  }
  .brand-main {
    display: block;
    font-size: 152px;
    line-height: 152px;
    letter-spacing: -2px;
    color: var(--ink);
  }
  .brand-sub {
    display: block;
    font-size: 69px;
    line-height: 72px;
    letter-spacing: 0.5px;
    text-transform: uppercase;
    color: var(--florist-green);
    margin-top: -2px;
  }
  .contact {
    position: absolute;
    right: 643px;
    top: 374px;
    text-align: right;
    font-style: normal;
    font-weight: 300;
    font-size: 32px;
    line-height: 44.5px;
    color: var(--ink);
  }
  .proprietors {
    position: absolute;
    right: 643px;
    top: 636px;
    font-weight: 300;
    font-size: 26px;
    letter-spacing: 0.3px;
    text-transform: uppercase;
    color: var(--florist-green);
    white-space: nowrap;
  }
  .social {
    position: absolute;
    left: 950px;
    top: 627px;
    display: flex;
    align-items: center;
    gap: 9px;
  }
  .social-square {
    width: 44px;
    height: 44px;
    background: var(--badge-dark);
  }
  .social-label {
    font-weight: 600;
    font-size: 18px;
    line-height: 20px;
    color: var(--ink);
  }
  .social-label .network {
    display: block;
    font-size: 27px;
    line-height: 28px;
  }
</style>
</head>
<body>
  <main class="card">
    <div class="leaf-panel" role="img" aria-label="Pale sage panel with a pattern of overlapping skeleton leaves"></div>

    <h1 class="brand">
      <span class="brand-main">Petals</span>
      <span class="brand-sub">on Larkmore</span>
    </h1>

    <address class="contact">
      41 Brindle Street<br>
      Ashvale Marrow 3871<br>
      Phone: 0352983047<br>
      Fax : 0352983066<br>
      pol@wrenmail.net.au
    </address>

    <p class="proprietors">Proprietors: Dana &amp; Lee Thornwick</p>

    <div class="social">
      <span class="social-square"></span>
      <span class="social-label">Find us on <span class="network">Friendlink</span></span>
    </div>
  </main>
</body>
</html>
```